Business Card and Word .doc header and footer required

I need a business card designed for my cybersecurity consulting company. Also required, is a header and footer to be ued for my word documents.
Attached is the Logo design, font and rgb used.

Industry/Entity Type

Cyber Security Consulting

Contact Information for Business Card

Name, Phone, email, website

Colors
0054AA
0677BA
7BADD7
CADEEF
E8F1F8

Requirements
Must have
• Sleek, modern

```html
<!DOCTYPE html>
<html lang="en">
<head>
<meta charset="utf-8">
<title>Harbor Ridge Consulting – Business Card</title>
<link href="https://fonts.googleapis.com/css2?family=Montserrat:wght@400;500;700&display=swap" rel="stylesheet">
<style>
  :root {
    --backdrop: #3a3b3e;
    --card: #0c1226;
    --brand-blue: #1a8fd0;
    --silver: #c9ccd1;
    --ink-light: #f2f4f7;
  }
  * { margin: 0; padding: 0; box-sizing: border-box; }
  html, body {
    width: 1200px; height: 998px; overflow: hidden;
    background: var(--backdrop);
    font-family: "Montserrat", sans-serif;
  }
  .card {
    position: absolute; left: 250px; width: 700px; height: 400px;
    background: var(--card);
    box-shadow: 0 10px 30px rgba(0,0,0,.45);
  }
  .card--front { top: 70px; display: flex; align-items: center; justify-content: center; }
  .card--back { top: 528px; display: flex; align-items: center; }

  .brand { display: flex; flex-direction: column; align-items: center; gap: 22px; }
  .brand__dot { width: 78px; height: 78px; border-radius: 50%; border: 6px solid currentColor; }
  .brand__name {
    font-weight: 700; font-size: 34px; letter-spacing: 1px; line-height: 1.2;
    text-transform: uppercase; text-align: center;
  }
  .card--front .brand { color: var(--silver); opacity: .5; }
  .card--back .brand { color: var(--silver); width: 340px; }
  .card--back .brand__name { font-size: 30px; }

  .divider { width: 2px; height: 230px; background: var(--brand-blue); opacity: .8; }

  .contact { padding-left: 38px; color: var(--ink-light); }
  .contact__name { color: var(--brand-blue); font-weight: 700; font-size: 31px; line-height: 1.1; text-transform: uppercase; }
  .contact__role { font-size: 17px; margin: 6px 0 20px; }
  .contact__list { list-style: none; }
  .contact__item { display: flex; align-items: center; gap: 14px; font-size: 16px; margin-bottom: 9px; }
  .contact__item svg { width: 16px; height: 16px; fill: var(--brand-blue); flex: none; }
  .contact__address { font-size: 16px; line-height: 1.45; margin-top: 16px; }
</style>
</head>
<body>
  <section class="card card--front">
    <div class="brand">
      <span class="brand__dot"></span>
      <span class="brand__name">Harbor Ridge<br>Consulting</span>
    </div>
  </section>

  <section class="card card--back">
    <div class="brand">
      <span class="brand__dot"></span>
      <span class="brand__name">Harbor Ridge<br>Consulting</span>
    </div>
    <div class="divider"></div>
    <div class="contact">
      <h1 class="contact__name">Daniel Brooks</h1>
      <p class="contact__role">Managing Director</p>
      <ul class="contact__list">
        <li class="contact__item">
          <svg viewBox="0 0 24 24" aria-hidden="true"><path d="M6.6 10.8a15.1 15.1 0 0 0 6.6 6.6l2.2-2.2c.3-.3.7-.4 1-.2 1.1.4 2.3.6 3.6.6.6 0 1 .4 1 1V20c0 .6-.4 1-1 1A17 17 0 0 1 3 4c0-.6.4-1 1-1h3.5c.6 0 1 .4 1 1 0 1.3.2 2.5.6 3.6.1.3 0 .7-.2 1z"/></svg>
          041-555 208 316
        </li>
        <li class="contact__item">
          <svg viewBox="0 0 24 24" aria-hidden="true"><path d="M2 5h20v14H2zm2 2v.5l8 5 8-5V7l-8 5z"/></svg>
          info@harborridge.com
        </li>
        <li class="contact__item">
          <svg viewBox="0 0 24 24" aria-hidden="true"><path d="M12 2a10 10 0 1 0 0 20 10 10 0 0 0 0-20zm0 2c1.2 0 2.6 2.3 3 6H9c.4-3.7 1.8-6 3-6zm-3 8h6c-.2 4-1.7 8-3 8s-2.8-4-3-8zm-4.9-2a8 8 0 0 1 5-5.6C8.5 6 8 8 7.9 10zm0 2h3.8c.1 2.3.6 4.3 1.2 5.6A8 8 0 0 1 4.1 12zm12-2c-.1-2-.6-4-1.2-5.6a8 8 0 0 1 5 5.6zm0 2h3.8a8 8 0 0 1-5 5.6c.6-1.3 1.1-3.3 1.2-5.6z"/></svg>
          www.harborridge.com
        </li>
      </ul>
      <p class="contact__address">18 Quay Street<br>Portland, 04101</p>
    </div>
  </section>
</body>
</html>
```